Tumblewick Youth Sports Academy

I need a family friendly website for children's sports coaching, diets and the importance of children's nutrition, child minding services,children's councilling and physiology services.
Also once I have an understanding of numbers and my fees I will offer a pick up service for my classes

Please add my new logo which is my buisness name,

Target Market(s)

Children of all ages and parents who would like there kids involved in sporting programmes ,

Industry/Entity Type

Nutrition

Requirements
Must have
• Active kids are healthy kids..
Also the logo I have uploaded .
Skype and video calls available for parents to see child's progress and safety at classes if parents are unable to attend.
Nice to have
• Listed about the services I will be offering,
One on one and group sessions.child minding and nanny services, parent and child councilling and physcology services,diet and nutrition personalisation services,pick up services,school visits and motivational classes,
Fully covered and insured business,

```html
<!DOCTYPE html>
<html lang="en">
<head>
<meta charset="utf-8">
<title>Tumblewick Youth Sports Academy</title>
<link rel="stylesheet" href="https://fonts.googleapis.com/css2?family=PT+Sans+Narrow:wght@400;700&display=swap">
<style>
  :root {
    --sky: #5d9fe0;
    --grass: #7aa33a;
    --grass-dark: #4f7a22;
    --nav-bg: #f4f7f9;
    --nav-border: #161616;
    --accent-orange: #f6b858;
    --heading-brown: #5a4312;
    --text-brown: #3c2a10;
    --alert-red: #e8262a;
    --promo-red: #e5161b;
    --promo-green: #6cc21c;
    --footer-brown: #361c04;
    --white: #ffffff;
    --ink: #111111;
  }
  * { box-sizing: border-box; margin: 0; padding: 0; }
  html, body { width: 1200px; height: 1146px; overflow: hidden; }
  body {
    position: relative;
    font-family: "PT Sans Narrow", "Arial Narrow", sans-serif;
    color: var(--text-brown);
    background: var(--grass);
  }
  .field-backdrop {
    position: absolute; inset: 0 0 131px 0;
    background: linear-gradient(180deg, var(--sky) 0%, #9cc6ea 30%, #8eb655 42%, var(--grass) 65%, var(--grass-dark) 100%);
  }
  .main-nav {
    position: absolute; left: 120px; top: 0; width: 962px; height: 80px;
    background: var(--nav-bg);
    border-right: 6px solid var(--nav-border);
    border-bottom: 6px solid var(--nav-border);
    border-left: 6px solid var(--nav-border);
    display: flex; align-items: flex-start; padding-left: 14px;
  }
  .main-nav a {
    display: block; height: 70px; line-height: 74px; padding: 0 12px;
    font-size: 35px; font-weight: 700; color: var(--ink); text-decoration: none;
    margin-right: 2px;
  }
  .main-nav a.is-current { background: var(--accent-orange); padding: 0 16px; }
  .main-nav a.is-underlined { text-decoration: underline; text-underline-offset: 5px; }
  .phone-line {
    position: absolute; left: 782px; top: 86px; height: 44px;
    display: flex; align-items: center; gap: 4px;
    color: var(--white); font-size: 26px; font-weight: 700;
  }
  .hero-frame {
    position: absolute; left: 125px; top: 133px; width: 955px; height: 367px;
    background: var(--white); padding: 10px;
  }
  .hero-image {
    width: 100%; height: 100%;
    background: linear-gradient(100deg, #e8311c 0%, #f26a1c 35%, #7e9e3a 55%, #3b5fa8 75%, #6d8c3a 100%);
    position: relative;
  }
  .slide-pager {
    position: absolute; right: 16px; bottom: 10px; display: flex; gap: 14px;
    color: var(--white); font-size: 36px; font-weight: 700;
  }
  .slide-pager .is-active { text-decoration: underline; text-underline-offset: 4px; }
  .brand-mark {
    position: absolute; left: 116px; top: 80px; width: 176px;
    display: flex; align-items: center; gap: 6px;
  }
  .brand-mark .brand-dot {
    flex: none; width: 26px; height: 26px; border-radius: 50%; background: var(--alert-red);
  }
  .brand-mark .brand-name {
    font-size: 22px; font-weight: 700; line-height: 24px; color: var(--white);
  }
  .content-panel {
    position: absolute; left: 120px; top: 518px; width: 870px; height: 452px;
    background: var(--white); padding: 26px 20px 0 20px;
  }
  .content-panel h1, .content-panel h2 {
    font-size: 35px; font-weight: 700; color: var(--heading-brown); line-height: 40px;
  }
  .content-panel h1 .bang { color: var(--alert-red); }
  .intro-text {
    width: 568px; margin-top: 10px; font-size: 17px; line-height: 25px; color: var(--text-brown);
    letter-spacing: -0.3px; hyphens: auto;
  }
  .content-panel h2 { margin-top: 32px; }
  .service-columns {
    display: grid; grid-template-columns: 264px 260px; margin-top: 10px;
    list-style: none; font-size: 19px; line-height: 25.2px; color: var(--text-brown);
  }
  .service-columns li::before { content: "\2022"; margin-right: 3px; }
  .promo {
    position: absolute; left: 715px; width: 367px; color: var(--white);
    font-weight: 700; text-shadow: 2px 2px 0 rgba(0,0,0,0.35);
  }
  .promo-active {
    top: 535px; height: 182px; background: var(--promo-red);
    padding: 32px 0 0 20px; font-size: 50px; line-height: 56px;
  }
  .promo-active .promo-text { position: relative; }
  .heart-art {
    position: absolute; right: -14px; top: -32px; width: 146px; height: 124px;
    border-radius: 50% 50% 46% 46%;
    background: radial-gradient(circle at 40% 35%, #f0463c, #b5121a);
  }
  .promo-friend {
    top: 745px; height: 187px; background: var(--promo-green); text-align: center;
  }
  .promo-friend .line-top { font-size: 40px; margin-top: 16px; line-height: 46px; position: relative; }
  .promo-friend .line-bottom { font-size: 52px; line-height: 56px; margin-top: 47px; position: relative; }
  .handshake-art {
    position: absolute; left: 133px; top: 64px; width: 100px; height: 40px;
    border-radius: 20px; background: linear-gradient(180deg, #ffc24a, #f28c1a);
  }
  .site-footer {
    position: absolute; left: 0; top: 1015px; width: 1200px; height: 131px;
    background: var(--footer-brown); color: var(--white);
    font-size: 19px; line-height: 31px; text-align: center; padding-top: 31px;
  }
  .site-footer .footer-inner { width: 500px; margin-left: 275px; }
  .site-footer a { color: var(--white); }
</style>
</head>
<body>
  <div class="field-backdrop" role="img" aria-label="Sunny playing field with blue sky and children running across the grass"></div>

  <nav class="main-nav">
    <a href="#" class="is-current">HOME</a>
    <a href="#">SERVICES</a>
    <a href="#">GALLERY</a>
    <a href="#">ABOUT US</a>
    <a href="#" class="is-underlined">REGISTER</a>
    <a href="#">CONTACT US</a>
  </nav>

  <div class="phone-line">
    <svg width="62" height="44" viewBox="0 0 62 44" aria-hidden="true">
      <path d="M6 14 Q31 0 56 14 L52 22 L42 18 L40 12 Q31 9 22 12 L20 18 L10 22 Z" fill="#cfd8e0" stroke="#6b7a88" stroke-width="2"/>
      <rect x="14" y="22" width="34" height="18" rx="3" fill="#e4ebf1" stroke="#6b7a88" stroke-width="2"/>
      <rect x="22" y="26" width="18" height="10" fill="#f08a2a"/>
    </svg>
    <span>+44 (0) 1632 960 418</span>
  </div>

  <section class="hero-frame">
    <div class="hero-image" role="img" aria-label="Colourful camping tents and a motorbike on a grassy campsite">
      <div class="slide-pager"><span>1</span><span class="is-active">2</span><span>3</span><span>4</span></div>
    </div>
  </section>

  <div class="brand-mark">
    <span class="brand-dot"></span>
    <span class="brand-name">Tumblewick Youth Sports Academy</span>
  </div>

  <main class="content-panel">
    <h1>Welcome to Our Sports Academy<span class="bang">!</span></h1>
    <p class="intro-text">Lorem ipsum dolor sit amet, consectetur adipiscing elit. In feugiat nibh ac aliquam egestas. Praesent et ante in arcu posuere imperdiet. Donec egestas elit eget congue porttitor. Cum sociis natoque penatibus et magnis dis parturient montes, nascetur ridiculus mus. Pellentesque sodales varius eros, ac fermentum est elementum in. Vestibulum in velit et elit vehicula sollicitudin vel ac dui.</p>
    <h2>Our Services</h2>
    <ul class="service-columns">
      <li>Well Supervised Training Sessions</li>
      <li>Well Supervised Training Sessions</li>
      <li>Modern Equipment</li>
      <li>Child Minding Service</li>
      <li>First Aid Training</li>
      <li>First Aid Training</li>
      <li>Diet Planning</li>
      <li>Counselling</li>
      <li>Motivational Programs</li>
      <li>Live Progress Checking</li>
      <li>Pickup Services</li>
      <li>Physiology Services</li>
    </ul>
  </main>

  <aside class="promo promo-active">
    <div class="heart-art" role="img" aria-label="Red heart illustration with a heartbeat line"></div>
    <div class="promo-text">Active Kids<br>Are Healthy Kids</div>
  </aside>

  <aside class="promo promo-friend">
    <div class="handshake-art" role="img" aria-label="Cartoon handshake illustration"></div>
    <div class="line-top">Power of a Friend</div>
    <div class="line-bottom">The No Bully Zone</div>
  </aside>

  <footer class="site-footer">
    <div class="footer-inner">
      <div>Copyright Protected © 2014 , Tumblewick Youth Sports Academy</div>
      <div>Read <a href="#">Privacy Policy</a> and <a href="#">Terms and Conditions</a></div>
    </div>
  </footer>
</body>
</html>
```